We need a business card design for a new soccer program based in Melbourne, Victoria, Australia.
Coaching kids from 2 through to 14 develop social, motor and soccer skills, in a fun and friendly non-competitive environment.
Our company colours are blue and orange as seen in the logo attached below. However, we are happy for the font to be any modern colour that looks professional.
Target Market(s)
Mums and dads
Industry/Entity Type
Business
Contact Information for Business Card
business name: Bright Kick Soccer
Marco Delvani Director- 0491 375 618
Luke Fernholt Director- 0417 583 106
Tomas Wendhaus Head Coach
email: marco@brightkicksoccer.com.au
website: www.brightkicksoccer.com.au
Coaching kids from 2-14
https://www.facebook.com/brightkicksoccer (facebook page not required unless it looks good without being clustered)
Look and feel

```html
<!DOCTYPE html>
<html lang="en">
<head>
<meta charset="utf-8">
<title>Bright Kick Soccer – Business Card</title>
<link rel="stylesheet" href="https://fonts.googleapis.com/css2?family=Open+Sans:wght@600;700;800&display=swap">
<style>
  :root {
    --blue: #2f3a9e;
    --blue-deep: #232c80;
    --orange: #f07a1a;
    --orange-light: #f89236;
    --white: #ffffff;
    --ink: #111111;
    --silhouette: #1d1d26;
    --backdrop: #d9d9dc;
  }
  * { box-sizing: border-box; margin: 0; padding: 0; }
  html, body { width: 1200px; height: 778px; overflow: hidden; }
  body {
    background: var(--backdrop);
    font-family: "Open Sans", sans-serif;
    position: relative;
  }
  .card {
    position: absolute;
    top: 234px;
    width: 540px;
    height: 309px;
    overflow: hidden;
    box-shadow: 0 6px 18px rgba(0,0,0,.25);
  }
  .card-front { left: 40px; }
  .card-back { left: 620px; }
  .card-bg { position: absolute; inset: 0; width: 100%; height: 100%; }

  .brand {
    position: absolute;
    display: flex;
    align-items: center;
    gap: 10px;
    color: var(--orange);
    font-weight: 800;
    line-height: 0.95;
  }
  .brand-dot {
    width: 26px; height: 26px;
    border-radius: 50%;
    background: var(--orange);
    flex: none;
  }
  .card-front .brand { left: 28px; top: 56px; font-size: 30px; }
  .card-back .brand { right: 34px; top: 40px; font-size: 38px; }
  .card-back .brand-dot { width: 34px; height: 34px; }

  .tagline {
    position: absolute;
    font-weight: 700;
  }
  .card-front .tagline {
    left: 248px; top: 118px;
    font-size: 22px;
    color: var(--orange);
  }
  .card-back .tagline {
    left: 30px; bottom: 30px;
    font-size: 17px;
    color: var(--ink);
  }

  .people {
    position: absolute;
    left: 30px; top: 170px;
    color: var(--white);
  }
  .person { margin-bottom: 7px; }
  .person-name { font-size: 17px; font-weight: 700; line-height: 1.2; }
  .person-role { font-size: 13px; font-weight: 600; color: var(--orange); line-height: 1.2; }

  .contacts {
    position: absolute;
    right: 24px; top: 184px;
    list-style: none;
    color: var(--white);
    font-size: 14px;
    font-weight: 600;
    text-align: right;
  }
  .contacts li {
    display: flex;
    justify-content: flex-end;
    align-items: center;
    gap: 8px;
    height: 24px;
  }
  .contact-icon { width: 17px; height: 17px; flex: none; }

  .player-figure {
    position: absolute;
    left: 120px; top: 100px;
    width: 170px; height: 150px;
    border-radius: 50% 40% 45% 35%;
    background: var(--silhouette);
    opacity: .9;
  }
</style>
</head>
<body>

<section class="card card-front" aria-label="Card front with contact details">
  <svg class="card-bg" viewBox="0 0 540 309" preserveAspectRatio="none" aria-hidden="true">
    <defs>
      <linearGradient id="front-blue" x1="0" y1="0" x2="0" y2="1">
        <stop offset="0" stop-color="#3a46b0"/>
        <stop offset="1" stop-color="#262f88"/>
      </linearGradient>
    </defs>
    <rect width="540" height="309" fill="url(#front-blue)"/>
    <polygon points="0,0 540,0 540,62 0,142" fill="#ffffff"/>
    <polygon points="0,142 540,62 540,74 0,154" fill="#f07a1a"/>
  </svg>

  <div class="brand"><span class="brand-dot"></span><span>Bright Kick<br>Soccer</span></div>
  <p class="tagline">Coaching kids from 2-14</p>

  <div class="people">
    <div class="person">
      <p class="person-name">Tomas Wendhaus</p>
      <p class="person-role">Head Coach</p>
    </div>
    <div class="person">
      <p class="person-name">Marco Delvani</p>
      <p class="person-role">Director</p>
    </div>
    <div class="person">
      <p class="person-name">Luke Fernholt</p>
      <p class="person-role">Director</p>
    </div>
  </div>

  <ul class="contacts">
    <li>marco@brightkicksoccer.com.au
      <svg class="contact-icon" viewBox="0 0 20 20" aria-hidden="true"><rect x="1.5" y="4" width="17" height="12" fill="none" stroke="#f07a1a" stroke-width="2"/><path d="M2 5 L10 11 L18 5" fill="none" stroke="#f07a1a" stroke-width="2"/></svg>
    </li>
    <li>www.brightkicksoccer.com
      <svg class="contact-icon" viewBox="0 0 20 20" aria-hidden="true"><circle cx="10" cy="10" r="8" fill="none" stroke="#f07a1a" stroke-width="2"/><ellipse cx="10" cy="10" rx="3.5" ry="8" fill="none" stroke="#f07a1a" stroke-width="1.6"/><path d="M2 10 H18" stroke="#f07a1a" stroke-width="1.6"/></svg>
    </li>
    <li>0417 583 106
      <svg class="contact-icon" viewBox="0 0 20 20" aria-hidden="true"><path d="M4 3 L8 3 L9 7 L7 8.5 C8 11 9 12 11.5 13 L13 11 L17 12 L17 16 C10 17 3 10 4 3 Z" fill="#f07a1a"/></svg>
    </li>
  </ul>
</section>

<section class="card card-back" aria-label="Card back">
  <svg class="card-bg" viewBox="0 0 540 309" preserveAspectRatio="none" aria-hidden="true">
    <defs>
      <linearGradient id="back-orange" x1="0" y1="0" x2="1" y2="1">
        <stop offset="0" stop-color="#f89236"/>
        <stop offset="1" stop-color="#e9680e"/>
      </linearGradient>
    </defs>
    <rect width="540" height="309" fill="#2f3a9e"/>
    <polygon points="0,252 540,140 540,309 0,309" fill="url(#back-orange)"/>
  </svg>

  <div class="player-figure" role="img" aria-label="Silhouette of a young player kicking a ball"></div>
  <div class="brand"><span class="brand-dot"></span><span>Bright Kick<br>Soccer</span></div>
  <p class="tagline">Coaching kids from 2-14</p>
</section>

</body>
</html>
```